Anzeigengestaltung für einen einen ambulanten Pflegedienst
Zielgruppe
Insgesamt möchte ich gern drei Anzeigen für das Internet gestalten haben. Ich betreibe einen ambulanten Pflegedienst. Die erste Anzeige soll dazu dienen Kunden anzusprechen, die einen Unterstützungsbedarf und / oder einen Beratungsbedarf haben. Die zweite Anzeige soll dazu dienen neues Personal anzuwerben. Die dritte Anzeige soll speziell potenzielle Azubis ansprechen. Die Anzeigen sind gedacht für Chatterwall und Pixelora hauptsächlich. In den Druck sollte es schon 10cm x 8cm sein. Es wäre super wenn vielleicht auch eine Art Aufruf an ehrenamtliche Mitarbeiter erfolgt.
Aufgabenstellung
Die Anzeigen sollen den Stil der Homepage beibehalten. Freundlich, frisch und agil wirken. Alle sollten emotional ansprechend sein und gerade der für zukünftige Mitarbeiter sollte deutlich ein gutes Betriebsklima vermitteln. Als Datei habe ich einige Bilder, die bereits für die Homepage oder Flyer verwendet wurden hochgeladen. des Weiteren habe ich die einzelnen Seiten des Flyers hochgeladen.

```html
<!DOCTYPE html>
<html lang="de">
<head>
<meta charset="utf-8">
<title>Weidenhof Pflege – Anzeigen</title>
<link href="https://fonts.googleapis.com/css2?family=Anton&family=Raleway:wght@400;500;600;700&display=swap" rel="stylesheet">
<style>
  :root {
    --stage: #bfbfbf;
    --paper: #ffffff;
    --green: #7aae3c;
    --blue: #29a6e0;
    --teal: #4db0ad;
    --teal-text: #3aa6a2;
    --ink: #1e1e1e;
    --grey-name: #555759;
    --cross: #f0f0f0;
  }
  * { box-sizing: border-box; margin: 0; padding: 0; }
  html, body { width: 1200px; height: 1117px; overflow: hidden; background: var(--stage); }
  body { position: relative; font-family: "Raleway", sans-serif; color: var(--ink); }

  .ad {
    position: absolute; width: 543px; height: 435px; background: var(--paper);
    overflow: hidden; box-shadow: 2px 3px 6px rgba(0,0,0,0.25);
  }
  .ad--care { left: 50px; top: 121px; }
  .ad--courses { left: 611px; top: 121px; }
  .ad--jobs { left: 328px; top: 572px; }

  .ad__shapes { position: absolute; inset: 0; width: 543px; height: 435px; }

  .brand { position: absolute; left: 0; top: 30px; width: 296px; text-align: center; }
  .brand__dot {
    display: block; width: 74px; height: 74px; margin: 4px auto 26px;
    border-radius: 50%; background: var(--teal);
  }
  .brand__name {
    font-weight: 500; font-size: 33px; letter-spacing: 0.5px;
    color: var(--grey-name); line-height: 1;
  }

  .ad__kicker {
    position: absolute; left: 0; right: 0; text-align: center;
    color: var(--teal-text); font-size: 17.5px; font-weight: 500; line-height: 1;
  }
  .ad__headline {
    position: absolute; left: 0; right: 0; text-align: center;
    font-family: "Anton", sans-serif; font-weight: 400; color: var(--ink);
    line-height: 1;
  }
  .ad__headline span { display: inline-block; transform-origin: center; }
  .ad__body {
    position: absolute; left: 36px; right: 36px; text-align: center;
    font-size: 9.6px; line-height: 11.5px; font-weight: 500;
  }
  .ad__url {
    position: absolute; left: 0; right: 0; top: 409px; text-align: center;
    color: #fff; font-weight: 700; font-size: 12.5px; line-height: 14px;
  }

  .ad--care .ad__kicker { top: 264px; }
  .ad--courses .ad__kicker { top: 258px; }
  .ad--jobs .ad__kicker { top: 256px; }

  .ad--care .ad__headline { top: 286px; font-size: 38px; }
  .ad--care .ad__headline span { transform: scaleX(0.84); }
  .ad--courses .ad__headline { top: 281px; font-size: 49px; }
  .ad--courses .ad__headline span { transform: scaleX(0.85); }
  .ad--jobs .ad__headline { top: 275px; font-size: 46px; }
  .ad--jobs .ad__headline span { transform: scaleX(0.95); }

  .ad--care .ad__body { top: 333px; left: 40px; right: 40px; }
  .ad--courses .ad__body { top: 338px; left: 52px; right: 52px; }

  .skills { position: absolute; top: 338px; left: 0; right: 0; height: 40px; }
  .skills__col { position: absolute; top: 0; list-style: none; font-size: 12px; font-weight: 500; line-height: 20px; }
  .skills__col:nth-child(1) { left: 52px; }
  .skills__col:nth-child(2) { left: 185px; }
  .skills__col:nth-child(3) { left: 343px; }
  .skills__col li { position: relative; padding-left: 17px; }
  .skills__col li svg { position: absolute; left: 0; top: 5px; }
  .skills__rule { position: absolute; top: 3px; width: 1px; height: 30px; background: var(--teal); }
  .skills__rule--a { left: 171px; }
  .skills__rule--b { left: 328px; }
</style>
</head>
<body>

<section class="ad ad--care">
  <svg class="ad__shapes" viewBox="0 0 900 720" preserveAspectRatio="none">
    <defs>
      <linearGradient id="photoCare" x1="0" y1="0" x2="1" y2="1">
        <stop offset="0" stop-color="#e6e2dc"/><stop offset="1" stop-color="#8f959c"/>
      </linearGradient>
    </defs>
    <path role="img" aria-label="Foto: Pflegerin tröstet einen älteren Patienten" fill="url(#photoCare)" d="M425 0 L900 0 L900 430 C760 335 620 305 480 300 C560 190 520 80 425 0 Z"/>
    <path fill="var(--green)" d="M0 400 C250 270 650 290 900 440 L900 452 C650 310 250 300 0 462 Z"/>
    <path fill="var(--blue)" d="M0 468 C250 320 650 315 900 458 L900 530 C680 360 230 350 0 468 Z"/>
    <g fill="var(--cross)">
      <path d="M765 635 h35 v-35 h35 v35 h35 v35 h-35 v50 h-35 v-50 h-35 Z"/>
      <path d="M738 635 h10 v-10 h10 v10 h10 v10 h-10 v10 h-10 v-10 h-10 Z"/>
    </g>
    <ellipse cx="450" cy="740" rx="265" ry="95" fill="var(--teal)"/>
  </svg>
  <div class="brand"><span class="brand__dot"></span><p class="brand__name">WEIDENHOF</p></div>
  <p class="ad__kicker">Wir zählen auf Dich</p>
  <h2 class="ad__headline"><span>WAS WIRD AUF DICH ZUKOMMEN?</span></h2>
  <p class="ad__body">Die ambulante Pflege wird in der Häuslichkeit der Patienten durchgeführt. Es ist unser Ziel die Pflege für alle Beteiligten so würdevoll und respektvoll zu gestalten wie möglich. Der zu betreuende Mensch steht dabei im Vordergrund, daher gewähren wir jedem die Zeit, die er braucht.</p>
  <p class="ad__url">www.weidenhof-pflege.de</p>
</section>

<section class="ad ad--courses">
  <svg class="ad__shapes" viewBox="0 0 900 720" preserveAspectRatio="none">
    <defs>
      <linearGradient id="photoCourses" x1="0" y1="0" x2="1" y2="1">
        <stop offset="0" stop-color="#eef0f2"/><stop offset="1" stop-color="#b8a99c"/>
      </linearGradient>
    </defs>
    <path role="img" aria-label="Foto: Pflegeteam legt die Hände in der Mitte zusammen" fill="url(#photoCourses)" d="M395 0 L900 0 L900 430 C760 335 620 305 480 300 C560 190 500 80 395 0 Z"/>
    <path fill="var(--green)" d="M0 400 C250 270 650 290 900 440 L900 452 C650 310 250 300 0 462 Z"/>
    <path fill="var(--blue)" d="M0 468 C250 320 650 315 900 458 L900 530 C680 360 230 350 0 468 Z"/>
    <g fill="var(--cross)">
      <path d="M765 635 h35 v-35 h35 v35 h35 v35 h-35 v50 h-35 v-50 h-35 Z"/>
      <path d="M738 635 h10 v-10 h10 v10 h10 v10 h-10 v10 h-10 v-10 h-10 Z"/>
    </g>
    <ellipse cx="450" cy="740" rx="265" ry="95" fill="var(--teal)"/>
  </svg>
  <div class="brand"><span class="brand__dot"></span><p class="brand__name">WEIDENHOF</p></div>
  <p class="ad__kicker">Unser Schulungsangebot für Sie</p>
  <h2 class="ad__headline"><span>PFLEGEKURSE</span></h2>
  <p class="ad__body">Sie sind pflegende*r Angehörige*r und möchten lernen, besser mit der Erkrankung der/des Pflegebedürftige*n umzugehen und die Pflege allgemein effektiver und belastungarmer zur gestalten? Dann sind Sie bei uns genau richtig</p>
  <p class="ad__url">www.weidenhof-pflege.de</p>
</section>

<section class="ad ad--jobs">
  <svg class="ad__shapes" viewBox="0 0 900 720" preserveAspectRatio="none">
    <defs>
      <linearGradient id="photoJobs" x1="0" y1="0" x2="1" y2="1">
        <stop offset="0" stop-color="#d8dde2"/><stop offset="0.6" stop-color="#5f95c8"/><stop offset="1" stop-color="#3a4450"/>
      </linearGradient>
    </defs>
    <path role="img" aria-label="Foto: junges Pflegeteam in blauer Dienstkleidung im Klinikflur" fill="url(#photoJobs)" d="M430 0 L900 0 L900 430 C760 335 620 305 480 300 C540 190 520 80 430 0 Z"/>
    <path fill="var(--green)" d="M0 400 C250 270 650 290 900 440 L900 452 C650 310 250 300 0 462 Z"/>
    <path fill="var(--blue)" d="M0 468 C250 320 650 315 900 458 L900 530 C680 360 230 350 0 468 Z"/>
    <g fill="var(--cross)">
      <path d="M730 635 h35 v-35 h35 v35 h35 v35 h-35 v50 h-35 v-50 h-35 Z"/>
      <path d="M676 668 h10 v-10 h10 v10 h10 v10 h-10 v10 h-10 v-10 h-10 Z"/>
    </g>
    <ellipse cx="450" cy="740" rx="265" ry="95" fill="var(--teal)"/>
  </svg>
  <div class="brand"><span class="brand__dot"></span><p class="brand__name">WEIDENHOF</p></div>
  <p class="ad__kicker">Wir suchen Dich!</p>
  <h2 class="ad__headline"><span>WAS BRINGST DU MIT?</span></h2>
  <div class="skills">
    <ul class="skills__col">
      <li><svg width="11" height="9" viewBox="0 0 11 9"><path d="M1 4.5 L4 7.5 L10 1" fill="none" stroke="var(--green)" stroke-width="2.2"/></svg>Teamfähigkeit</li>
      <li><svg width="11" height="9" viewBox="0 0 11 9"><path d="M1 4.5 L4 7.5 L10 1" fill="none" stroke="var(--green)" stroke-width="2.2"/></svg>Hilfsbereitschaft</li>
    </ul>
    <ul class="skills__col">
      <li><svg width="11" height="9" viewBox="0 0 11 9"><path d="M1 4.5 L4 7.5 L10 1" fill="none" stroke="var(--green)" stroke-width="2.2"/></svg>Engagement</li>
      <li><svg width="11" height="9" viewBox="0 0 11 9"><path d="M1 4.5 L4 7.5 L10 1" fill="none" stroke="var(--green)" stroke-width="2.2"/></svg>Führerschein Klasse B</li>
    </ul>
    <ul class="skills__col">
      <li><svg width="11" height="9" viewBox="0 0 11 9"><path d="M1 4.5 L4 7.5 L10 1" fill="none" stroke="var(--green)" stroke-width="2.2"/></svg>Gute Deutschkenntnisse</li>
      <li><svg width="11" height="9" viewBox="0 0 11 9"><path d="M1 4.5 L4 7.5 L10 1" fill="none" stroke="var(--green)" stroke-width="2.2"/></svg>in Wort und Schrift</li>
    </ul>
    <span class="skills__rule skills__rule--a"></span>
    <span class="skills__rule skills__rule--b"></span>
  </div>
  <p class="ad__url">www.weidenhof-pflege.de</p>
</section>

</body>
</html>
```